Business cards Dör Kornhüüs GmbH & Co.KG

We need a uniform business card design template for our employees.
A template should be created to have the same design for all business cards.

Contact Information for Business Card

Firma und Firmierung, Name, Funktion in Unternehmen, Anschrift, Tel. Handynummer, Emailadresse, Internetseite

Colors

Designer to choose colors to be used in the design.

Requirements
Must have
• Our company logo must be on it

```html
<!DOCTYPE html>
<html lang="de">
<head>
<meta charset="utf-8">
<title>Dör Kornhüüs – Visitenkarte</title>
<link rel="stylesheet" href="https://fonts.googleapis.com/css2?family=Arimo:wght@400&display=swap">
<style>
  :root {
    --stage: #d5d5d5;
    --card: #1b1b1b;
    --rose: #ef6f7c;
    --lilac: #c9a0d0;
    --text-font: "Arimo", Arial, sans-serif;
  }
  * { margin: 0; padding: 0; box-sizing: border-box; }
  html, body { width: 1000px; height: 1200px; overflow: hidden; }
  body {
    background: radial-gradient(ellipse at center, #dedede 0%, var(--stage) 70%, #cbcbcb 100%);
    position: relative;
    font-family: var(--text-font);
  }
  .card {
    position: absolute;
    background: var(--card);
    box-shadow: 0 8px 22px rgba(0,0,0,.45);
  }
  .card--front { left: 111px; top: 120px; width: 777px; height: 446px; }
  .card--back  { left: 109px; top: 633px; width: 782px; height: 447px; }

  .brand-name {
    position: absolute;
    color: var(--rose);
    font-weight: 400;
    white-space: nowrap;
    line-height: 1;
  }
  .card--front .brand-name { left: 57px; top: 98px; font-size: 46px; }
  .card--back .brand-name {
    left: 0; right: 0; top: 200px; text-align: center; font-size: 58px;
  }

  .holder { position: absolute; right: 53px; top: 222px; text-align: right; }
  .holder__name { color: var(--rose); font-size: 25px; line-height: 1; }
  .holder__role { color: var(--lilac); font-size: 16px; margin-top: 9px; }

  .divider {
    position: absolute; left: 57px; right: 53px; top: 291px;
    height: 2px; background: var(--lilac);
  }

  .contact-list { position: absolute; left: 57px; top: 313px; list-style: none; }
  .contact-list li {
    display: flex; align-items: center; gap: 9px;
    height: 25px; color: var(--lilac); font-size: 17px;
  }
  .contact-list svg { width: 17px; height: 17px; flex: none; }

  .address {
    position: absolute; right: 53px; top: 337px; text-align: right;
    color: var(--lilac); font-size: 17px; line-height: 25px; font-style: normal;
  }

  .accent-band { position: absolute; left: 0; bottom: 0; width: 777px; height: 19px; }
</style>
</head>
<body>

<section class="card card--front">
  <div class="brand-name">Dör Kornhüüs</div>

  <div class="holder">
    <div class="holder__name">Johnathon Doe</div>
    <div class="holder__role">Owner</div>
  </div>

  <div class="divider"></div>

  <ul class="contact-list">
    <li>
      <svg viewBox="0 0 24 24" aria-hidden="true"><path fill="#ef6f7c" d="M6.6 10.8a15.1 15.1 0 0 0 6.6 6.6l2.2-2.2a1 1 0 0 1 1-.25 11.4 11.4 0 0 0 3.6.6 1 1 0 0 1 1 1V20a1 1 0 0 1-1 1A17 17 0 0 1 3 4a1 1 0 0 1 1-1h3.5a1 1 0 0 1 1 1c0 1.25.2 2.45.6 3.6a1 1 0 0 1-.25 1z"/></svg>
      000.123.456.789
    </li>
    <li>
      <svg viewBox="0 0 24 24" aria-hidden="true"><rect x="6" y="2" width="12" height="20" rx="2" fill="none" stroke="#ef6f7c" stroke-width="2"/><circle cx="12" cy="18.5" r="1" fill="#ef6f7c"/></svg>
      000.123.456.789
    </li>
    <li>
      <svg viewBox="0 0 24 24" aria-hidden="true"><rect x="2" y="5" width="20" height="14" fill="#ef6f7c"/><path d="M2 5l10 8 10-8M2 19l7-6M22 19l-7-6" fill="none" stroke="#1b1b1b" stroke-width="1.6"/></svg>
      info@yourwebsitename.com
    </li>
    <li>
      <svg viewBox="0 0 24 24" aria-hidden="true"><g fill="none" stroke="#ef6f7c" stroke-width="1.8"><circle cx="12" cy="12" r="9.5"/><ellipse cx="12" cy="12" rx="4" ry="9.5"/><path d="M2.5 12h19M4 7h16M4 17h16"/></g></svg>
      www.yourwebsitename.com
    </li>
  </ul>

  <address class="address">
    4567 Lindenweg<br>
    Suite 123<br>
    Fairbrook, MD 21500
  </address>

  <svg class="accent-band" viewBox="0 0 777 19" preserveAspectRatio="none" aria-hidden="true">
    <polygon points="0,0 390,0 372,19 0,19" fill="#c9a0d0"/>
    <polygon points="402,0 777,0 777,19 384,19" fill="#ef6f7c"/>
  </svg>
</section>

<section class="card card--back">
  <div class="brand-name">Dör Kornhüüs</div>
</section>

</body>
</html>
```